Professional Business Card - TWO SIDES

I need a new business card design to be used by myself and my employees. I would like a professional card and for the front I thought I would like a dark blue thatch with our logo in a raised gold foil on top of it. On the other side I would like name, position, and contact info. I've uploaded our old design for an example of the info used.

Target Market(s)

Business Clients

Industry/Entity Type

CPA Firm

Contact Information for Business Card

Logo, Name, Title, Address, Phone Numbers, Website address, Email Address

Font styles to use
Serif
Sans Serif

Colors
0054AA
0677BA
7BADD7
CADEEF
E8F1F8
0094D4
00A9DD
6FCCEA
C7EBF8
E9F6FB

Requirements
Must have
• Modern Professional Look
Nice to have
• Logo in Gold Foil or ability to have is raised. I like our logo in a single color
Should not have
• I've uploaded old business card

```html
<!DOCTYPE html>
<html lang="en">
<head>
<meta charset="utf-8">
<title>Ashford &amp; Ashford – Business Card</title>
<link href="https://fonts.googleapis.com/css2?family=Arimo:wght@400;700&family=Saira+Semi+Condensed:wght@600&display=swap" rel="stylesheet">
<style>
  :root {
    --navy: #0d3a6e;
    --navy-deep: #0a2f5c;
    --lime: #a8cc2c;
    --white: #ffffff;
    --ink: #1a3f73;
    --rule: #9aa7b8;
    --stage: #2b2b2d;
  }
  * { margin: 0; padding: 0; box-sizing: border-box; }
  html, body { width: 1200px; height: 900px; overflow: hidden; }
  body {
    background: var(--stage);
    display: flex;
    flex-direction: column;
    align-items: center;
    justify-content: center;
    gap: 50px;
    font-family: "Arimo", Arial, sans-serif;
  }
  .card {
    position: relative;
    width: 630px;
    height: 360px;
    border-radius: 22px;
    overflow: hidden;
  }

  /* Front side */
  .card-front {
    background: linear-gradient(135deg, var(--navy-deep), var(--navy) 60%, #16508f);
  }
  .front-disc {
    position: absolute;
    left: 70px;
    top: 60px;
    width: 240px;
    height: 240px;
    border-radius: 50%;
    background: rgba(255,255,255,0.06);
  }
  .wordmark {
    font-family: "Saira Semi Condensed", "Arial Narrow", sans-serif;
    font-weight: 600;
    text-transform: uppercase;
    line-height: 1;
  }
  .wordmark-name { font-size: 46px; letter-spacing: 1px; }
  .wordmark-tag { font-size: 15px; letter-spacing: 4px; margin-top: 4px; }
  .card-front .wordmark {
    position: absolute;
    right: 50px;
    top: 140px;
    color: var(--white);
    text-align: right;
  }

  /* Back side */
  .card-back { background: var(--white); }
  .card-back .wordmark {
    position: absolute;
    left: 0; right: 0;
    top: 58px;
    text-align: center;
    color: var(--navy);
  }
  .identity {
    position: absolute;
    left: 150px;
    top: 172px;
    width: 190px;
    text-align: right;
  }
  .person-name { color: var(--lime); font-weight: 700; font-size: 28px; }
  .person-role { color: var(--ink); font-size: 19px; margin-top: 2px; }
  .divider {
    position: absolute;
    left: 362px;
    top: 162px;
    width: 1px;
    height: 80px;
    background: var(--rule);
  }
  .contacts {
    position: absolute;
    left: 382px;
    top: 164px;
    list-style: none;
    color: var(--ink);
    font-size: 17px;
  }
  .contacts li { display: flex; align-items: center; gap: 10px; height: 26px; }
  .contacts svg { width: 15px; height: 15px; flex: none; }

  .accent-strip {
    position: absolute;
    right: 0;
    top: 250px;
    height: 20px;
    width: 250px;
    display: flex;
    align-items: center;
  }
  .accent-navy { height: 100%; flex: 1; background: var(--navy); }
  .accent-dot {
    width: 24px; height: 24px; border-radius: 50%;
    background: var(--white); border: 4px solid var(--navy); flex: none;
  }
  .accent-lime { height: 100%; width: 90px; background: var(--lime); }

  .address-band {
    position: absolute;
    left: 0; right: 0;
    bottom: 40px;
    height: 42px;
    background: var(--navy);
    color: var(--white);
    font-size: 19px;
    display: flex;
    align-items: center;
    justify-content: center;
  }
</style>
</head>
<body>

  <section class="card card-front" aria-label="Card front">
    <div class="front-disc"></div>
    <div class="wordmark">
      <div class="wordmark-name">Ashford &amp; Ashford</div>
      <div class="wordmark-tag">Certified Public Accountants</div>
    </div>
  </section>

  <section class="card card-back" aria-label="Card back">
    <div class="wordmark">
      <div class="wordmark-name">Ashford &amp; Ashford</div>
      <div class="wordmark-tag">Certified Public Accountants</div>
    </div>

    <div class="identity">
      <div class="person-name">Daniel Reyes</div>
      <div class="person-role">Manager</div>
    </div>
    <div class="divider"></div>

    <ul class="contacts">
      <li>
        <svg viewBox="0 0 16 16"><path d="M3 1.5l3 .5 1 3-1.6 1.2a8 8 0 0 0 4.4 4.4L11 9l3 1 .5 3-1.8 1.5C7 14 2 9 1.5 3.3z" fill="#a8cc2c"/></svg>
        123-456-2100
      </li>
      <li>
        <svg viewBox="0 0 16 16" fill="none" stroke="#a8cc2c" stroke-width="1.6"><rect x="1.5" y="3.5" width="13" height="9" rx="1"/><path d="M2 4l6 5 6-5"/></svg>
        youremail@mailbox.com
      </li>
      <li>
        <svg viewBox="0 0 16 16" fill="none" stroke="#a8cc2c" stroke-width="1.4"><circle cx="8" cy="8" r="6.5"/><path d="M1.5 8h13M8 1.5c-3 3.5-3 9.5 0 13M8 1.5c3 3.5 3 9.5 0 13"/></svg>
        www.yourwebsite.com
      </li>
    </ul>

    <div class="accent-strip">
      <div class="accent-navy"></div>
      <div class="accent-dot"></div>
      <div class="accent-lime"></div>
    </div>

    <div class="address-band">Your address, city, state, ZIP 0000</div>
  </section>

</body>
</html>
```